Heronby Mortgage Capital Business Card

We need a business card design for our mortgage servicing company. In addition to servicing the loans of homeowners, we help homeowners with purchasing their homes and any mortgage refinancing. We would like to see designs that use the colors in the logo attached below (gold-ish yellow and navy blue), and any other design you deem fit! The design should communicate a simpler life with smart mortgages provided by Heronby.

```html
<!DOCTYPE html>
<html lang="en">
<head>
<meta charset="utf-8">
<title>Heronby Mortgage Capital – Business Card</title>
<link href="https://fonts.googleapis.com/css2?family=Lato:wght@400;700;900&family=Raleway:wght@300;400;700&display=swap" rel="stylesheet">
<style>
  :root {
    --navy: #25204b;
    --gold: #dfb13e;
    --backdrop: #559bb6;
    --paper: #ffffff;
  }
  * { box-sizing: border-box; margin: 0; padding: 0; }
  html, body { width: 1008px; height: 1200px; overflow: hidden; }
  body { background: var(--backdrop); position: relative; font-family: "Lato", sans-serif; color: var(--navy); }

  .card {
    position: absolute;
    background: var(--paper);
    box-shadow: 0 6px 18px rgba(20, 40, 55, 0.45);
    overflow: hidden;
  }
  .card--front { left: 115px; top: 112px; width: 777px; height: 442px; }
  .card--back  { left: 112px; top: 671px; width: 784px; height: 447px; }

  .brand {
    position: absolute;
    display: flex;
    align-items: center;
    gap: 12px;
    transform: translate(-50%, -50%);
    font-family: "Lato", sans-serif;
    font-weight: 900;
    color: var(--gold);
    white-space: nowrap;
    line-height: 1;
  }
  .brand__dot { border-radius: 50%; background: var(--gold); flex: none; }
  .card--front .brand { left: 203px; top: 198px; font-size: 52px; }
  .card--front .brand__dot { width: 18px; height: 18px; }
  .card--back .brand { left: 392px; top: 224px; font-size: 72px; }
  .card--back .brand__dot { width: 24px; height: 24px; }

  .person { position: absolute; right: 40px; top: 80px; text-align: right; }
  .person__name { font-family: "Raleway", sans-serif; font-size: 27px; letter-spacing: 0.2px; line-height: 1; }
  .person__first { font-weight: 700; }
  .person__last { font-weight: 300; }
  .person__role {
    display: inline-block;
    font-family: "Raleway", sans-serif;
    font-weight: 400;
    font-size: 19px;
    margin-top: 4px;
    padding-bottom: 4px;
    position: relative;
  }
  .person__role::after {
    content: "";
    position: absolute;
    right: 0; bottom: 0;
    width: 77px; height: 2px;
    background: var(--gold);
  }

  .contact { position: absolute; right: 40px; top: 186px; list-style: none; }
  .contact__item {
    display: flex;
    align-items: center;
    justify-content: flex-end;
    gap: 17px;
    font-size: 18px;
    line-height: 22px;
    text-align: right;
    margin-bottom: 14px;
  }
  .contact__item--address { margin-bottom: 20px; }
  .contact__item--phone { margin-bottom: 13px; }
  .contact__icon { width: 24px; height: 24px; flex: none; }

  .band { position: absolute; left: 0; bottom: 0; width: 777px; height: 32px; }

  .tab { position: absolute; top: 0; width: 32px; height: 447px; }
  .tab--left { left: 0; }
  .tab--right { right: 0; }
</style>
</head>
<body>

<section class="card card--front" aria-label="Card front">
  <div class="brand"><span class="brand__dot"></span>Heronby</div>

  <div class="person">
    <p class="person__name"><span class="person__first">DANIEL</span><span class="person__last">WHITCOMBE</span></p>
    <p class="person__role">Managing Director</p>
  </div>

  <ul class="contact">
    <li class="contact__item contact__item--address">
      <span>7312 Linden Park Avenue<br>Arlington, VA 22204</span>
      <svg class="contact__icon" viewBox="0 0 24 24" aria-hidden="true">
        <rect width="24" height="24" rx="3" fill="var(--navy)"/>
        <path d="M12 4.5a5 5 0 0 0-5 5c0 3.6 5 9.5 5 9.5s5-5.9 5-9.5a5 5 0 0 0-5-5z" fill="#fff"/>
        <circle cx="12" cy="9.6" r="2" fill="var(--navy)"/>
      </svg>
    </li>
    <li class="contact__item contact__item--phone">
      <span>+00 555 018 42</span>
      <svg class="contact__icon" viewBox="0 0 24 24" aria-hidden="true">
        <rect width="24" height="24" rx="3" fill="var(--navy)"/>
        <path d="M8.2 5.5l2 3.3-1.4 1.5c.8 1.9 2.1 3.2 4 4l1.5-1.4 3.3 2-.9 2.6c-5.6-.3-10-4.7-10.3-10.3z" fill="#fff"/>
      </svg>
    </li>
    <li class="contact__item">
      <span>contact@heronbymail.com</span>
      <svg class="contact__icon" viewBox="0 0 24 24" aria-hidden="true">
        <rect width="24" height="24" rx="3" fill="var(--navy)"/>
        <rect x="4.5" y="7" width="15" height="10.5" fill="#fff"/>
        <path d="M4.5 7l7.5 6 7.5-6M4.5 17.5l5.5-5M19.5 17.5l-5.5-5" stroke="var(--navy)" stroke-width="1.1" fill="none"/>
      </svg>
    </li>
    <li class="contact__item">
      <span>www.heronbymortgage.com</span>
      <svg class="contact__icon" viewBox="0 0 24 24" aria-hidden="true">
        <rect width="24" height="24" rx="3" fill="var(--navy)"/>
        <path d="M8 5v13l3.2-3 2.2 4.6 2-1-2.2-4.5h4.3z" fill="#fff"/>
      </svg>
    </li>
  </ul>

  <svg class="band" viewBox="0 0 777 32" preserveAspectRatio="none" aria-hidden="true">
    <polygon points="0,0 406,0 377,32 0,32" fill="var(--navy)"/>
    <polygon points="417,0 777,0 777,32 389,32" fill="var(--gold)"/>
  </svg>
</section>

<section class="card card--back" aria-label="Card back">
  <svg class="tab tab--left" viewBox="0 0 32 447" aria-hidden="true">
    <polygon points="0,104 32,121 32,328 0,344" fill="var(--gold)"/>
  </svg>
  <div class="brand"><span class="brand__dot"></span>Heronby</div>
  <svg class="tab tab--right" viewBox="0 0 32 447" aria-hidden="true">
    <polygon points="32,104 0,121 0,328 32,344" fill="var(--gold)"/>
  </svg>
</section>

</body>
</html>
```